Ironvale Shift Services

We are a underground coal mining labour hire company, needing a website that links into our online payroll (www.wagetrakker.com.au) and also need to have job applications page that is a preform with drop down menu,s with answers or check boxes. We would also need a 3 tier administration access for access to different files.
We are looking for an ongoing relationship with future app integration

Reason: There are a few more designs to come and I'm out at the mine for another week

Industry/Entity Type

Coal Mining

```html
<!DOCTYPE html>
<html lang="en">
<head>
<meta charset="utf-8">
<title>Ironvale Shift Services</title>
<link rel="stylesheet" href="https://fonts.googleapis.com/css2?family=Oswald:wght@300;400;500&family=Open+Sans:ital,wght@0,400;0,600;1,400&display=swap">
<style>
:root{
  --bg:#1b1b1b;
  --bg-deep:#121212;
  --header:#202020;
  --band:#242424;
  --orange:#f7941d;
  --orange-dark:#d9760c;
  --orange-soft:#f08a1c;
  --text:#d8d8d8;
  --muted:#a9a9a9;
  --white:#ffffff;
  --line:#3a3a3a;
  --button:#2c2c2c;
}
*{box-sizing:border-box;margin:0;padding:0}
html,body{width:1151px;height:1200px;overflow:hidden}
body{position:relative;background:radial-gradient(ellipse at 50% 45%,#2a2a2a 0%,var(--bg) 55%,var(--bg-deep) 100%);font-family:"Open Sans",Arial,sans-serif;color:var(--text)}
.abs{position:absolute}

/* header */
.site-header{left:0;top:0;width:1151px;height:89px;background:linear-gradient(#262626,var(--header))}
.brand{left:151px;top:26px;display:flex;align-items:center;gap:10px;font-family:"Oswald",sans-serif;font-weight:400;font-size:24px;color:var(--white)}
.brand-mark{width:30px;height:30px;border-radius:50%;background:var(--white)}
.phone{left:693px;top:34px;display:flex;align-items:center;gap:8px;font-family:"Oswald",sans-serif;font-weight:300;font-size:19px;color:var(--white)}
.social{left:860px;top:34px;display:flex;gap:10px}
.social span{width:26px;height:26px;border-radius:50%;background:#5a5a5a;display:block}

/* navigation */
.main-nav{left:0;top:89px;width:1151px;height:32px;background:var(--orange);border-bottom:1px solid #c46a0a}
.main-nav ul{list-style:none;position:absolute;left:147px;top:0;display:flex;height:32px}
.main-nav li{font-family:"Oswald",sans-serif;font-size:12px;color:var(--white);display:flex;align-items:center;justify-content:center;border-right:1px solid #e47f10;height:32px;text-transform:uppercase}
.main-nav li.active{background:var(--orange-dark)}

/* hero */
.hero{left:0;top:121px;width:1151px;height:310px;background:linear-gradient(100deg,#2a1a0c 0%,#6b4a1c 30%,#3a2c18 50%,#8a7a20 62%,#3a2a1a 75%,#7a1a14 88%,#1d1410 100%)}
.hero-title{left:147px;top:296px;font-family:"Oswald",sans-serif;font-weight:300;font-size:27px;letter-spacing:.5px;color:var(--white);text-transform:uppercase}
.hero-sub{left:149px;top:329px;font-style:italic;font-size:13px;color:var(--white)}
.hero-arrow{top:267px;width:34px;height:34px;border-radius:50%;border:2px solid #555;background:rgba(0,0,0,.35)}

/* services band */
.services{left:0;top:431px;width:1151px;height:82px;background:var(--band);border-bottom:1px solid var(--line)}
.service{top:449px;display:flex;gap:12px;align-items:flex-start}
.service-icon{width:34px;height:34px;border-radius:50%;border:2px solid #cfcfcf;flex:none;display:flex;align-items:center;justify-content:center}
.service h3{font-family:"Oswald",sans-serif;font-weight:400;font-size:18px;color:var(--white);line-height:1.1}
.service p{font-style:italic;font-size:9px;color:var(--orange);margin-top:2px}
.service-divider{top:446px;width:1px;height:48px;background:#3c3c3c}

/* intro */
.intro-title{left:151px;top:551px;display:flex;align-items:center;gap:8px;font-family:"Oswald",sans-serif;font-weight:400;font-size:21px;color:var(--white)}
.intro-title small{font-weight:300;font-size:17px}
.intro-mark{width:22px;height:22px;border-radius:50%;background:var(--white)}
.intro-text{left:151px;top:588px;width:522px;font-size:10px;line-height:14.5px;color:var(--text)}

.action{left:729px;width:267px;height:43px;background:var(--button);display:flex;align-items:center}
.action-icon{width:36px;height:43px;background:var(--orange);border-radius:0 22px 22px 0;flex:none}
.action div{margin-left:24px}
.action h4{font-family:"Oswald",sans-serif;font-weight:400;font-size:13px;color:var(--white);text-transform:uppercase;line-height:1.2}
.action p{font-size:11px;color:var(--white)}

/* cards */
.card{top:715px;width:213px}
.card-photo{width:213px;height:91px}
.card hr{border:0;border-top:1px solid #555;margin-top:13px}
.card h3{font-family:"Oswald",sans-serif;font-weight:400;font-size:13px;color:var(--white);margin-top:14px}
.card p{font-size:10px;line-height:14px;color:var(--muted);margin-top:4px}
.more{display:flex;align-items:center;gap:8px;margin-top:14px;font-size:10px;color:var(--text)}
.more span{width:15px;height:15px;background:var(--orange);display:flex;align-items:center;justify-content:center}

/* footer */
.footer-rule{left:0;top:1004px;width:1151px;height:1px;background:#2d2d2d}
.footer-ground{left:0;top:1005px;width:1151px;height:195px;background:linear-gradient(#181818 0%,#1f1f1f 60%,#2b2b2b 100%)}
.footer-col{top:1046px}
.footer-col h4{font-family:"Oswald",sans-serif;font-weight:400;font-size:13px;color:var(--white);text-transform:uppercase;padding-bottom:10px;border-bottom:1px solid #333;width:225px}
.menu-list{list-style:none;display:grid;grid-template-columns:122px 100px;row-gap:6px;margin-top:10px}
.menu-list li{font-size:10px;color:var(--text);padding-left:16px;position:relative}
.menu-list li::before{content:"";position:absolute;left:2px;top:4px;border-left:4px solid #ccc;border-top:3px solid transparent;border-bottom:3px solid transparent}
.news-item{display:flex;gap:24px;font-size:9px;line-height:13px;color:var(--text);padding:12px 0 10px 16px;border-bottom:1px solid #333;width:225px;position:relative}
.news-item::before{content:"";position:absolute;left:2px;top:16px;border-left:4px solid #ccc;border-top:3px solid transparent;border-bottom:3px solid transparent}
.news-item time{flex:none}
.contact-row{display:flex;gap:14px;font-size:9px;line-height:13px;color:var(--text);padding:12px 0;border-bottom:1px solid #333;width:225px}
.copyright{left:203px;top:1178px;font-size:10px;color:var(--text)}
</style>
</head>
<body>

<header class="site-header abs">
  <div class="brand abs"><span class="brand-mark"></span>Ironvale Shift Services</div>
  <div class="phone abs">
    <svg width="20" height="18" viewBox="0 0 20 18"><path d="M2 6c0-3 4-4 8-4s8 1 8 4v2h-4V6H6v2H2z" fill="#fff"/><rect x="4" y="9" width="12" height="8" rx="1" fill="#fff"/></svg>
    (123) 456 7890
  </div>
  <div class="social abs"><span></span><span></span><span></span><span></span></div>
</header>

<nav class="main-nav abs">
  <ul>
    <li class="active" style="width:106px">Home</li>
    <li style="width:136px">About us</li>
    <li style="width:134px">Employee pay</li>
    <li style="width:155px">SOP / WPI</li>
    <li style="width:144px">Contact us</li>
    <li style="width:176px">Mission statement</li>
  </ul>
</nav>

<section class="hero abs" role="img" aria-label="Underground coal miners with headlamps working beside yellow machinery and a surveyor in red overalls"></section>
<div class="hero-arrow abs" style="left:43px"></div>
<div class="hero-arrow abs" style="left:1073px"></div>
<h1 class="hero-title abs">Ironvale Shift Services</h1>
<p class="hero-sub abs">We are a underground coal mining labour hire company</p>

<section class="services abs"></section>
<div class="service abs" style="left:147px">
  <span class="service-icon"><svg width="18" height="18" viewBox="0 0 18 18"><path d="M4 14l4-4M10 4l4 4-4 4-4-4z" stroke="#ddd" stroke-width="2" fill="none"/></svg></span>
  <div><h3>Open cut electrical services</h3><p>Lorem ipsum dolor sit amet, consectetur adipiscing elit.</p></div>
</div>
<div class="service-divider abs" style="left:415px"></div>
<div class="service abs" style="left:449px">
  <span class="service-icon"><svg width="18" height="18" viewBox="0 0 18 18"><path d="M3 3l12 12M15 3L3 15" stroke="#ddd" stroke-width="2"/></svg></span>
  <div><h3>Open cut mechanical services</h3><p>Lorem ipsum dolor sit amet, consectetur adipiscing elit.</p></div>
</div>
<div class="service-divider abs" style="left:717px"></div>
<div class="service abs" style="left:755px">
  <span class="service-icon"><svg width="18" height="18" viewBox="0 0 18 18"><circle cx="9" cy="9" r="5" stroke="#ddd" stroke-width="2" fill="none"/><circle cx="9" cy="9" r="1.5" fill="#ddd"/></svg></span>
  <div><h3>Maintenance and relief services</h3><p>Lorem ipsum dolor sit amet, consectetur adipiscing elit.</p></div>
</div>

<h2 class="intro-title abs"><span class="intro-mark"></span>ISS <small>(Ironvale Shift Services)</small></h2>
<p class="intro-text abs">Lorem ipsum dolor sit amet, consectetur adipiscing elit. Aliquam ultricies odio magna. Mauris a lacus metus, sed ultrices dui. Vivamus at eros non lectus ultrices rutrum. Sed in neque diam. Nulla varius commodo justo, id consequat nisl lacinia vitae. Proin dictum tempus tellus, non consequat orci venes quis. Vestibulum rutrum dui sit amet nisi sollicitudin vitae dapibus nisl tincidunt. Sed in neque diam. Nulla varius commodo justo, id consequat nisl lacinia vitae. Proin dictum tempus tellus, non consequat orci venes quis. Vestibulum rutrum dui sit amet nisi sollicitudin vitae dapibus nisl tincidunt.</p>

<a class="action abs" style="top:556px"><span class="action-icon"></span><div><h4>Employment application form</h4><p>Click here for job applied</p></div></a>
<a class="action abs" style="top:615px"><span class="action-icon"></span><div><h4>Our online payroll system</h4><p>Click here for online pay</p></div></a>

<article class="card abs" style="left:203px">
  <div class="card-photo" role="img" aria-label="Two miners in hard hats beside underground equipment" style="background:linear-gradient(90deg,#5a4020,#b08040,#3a2a18)"></div>
  <hr><h3>Underground</h3>
  <p>Lorem ipsum dolor sit amet, consectetur adipiscing elit. Aliquam ultricies odio magna. Mauris a lacus metus, sed ultrices dui. Vivamus at eros non lectus ultrices rutrum. Sed in neque diam. Nulla varius commodo justo, id consequat nisl lacinia vitae. Proin</p>
  <div class="more"><span><svg width="7" height="8" viewBox="0 0 7 8"><path d="M1 1l4 3-4 3" stroke="#fff" stroke-width="1.5" fill="none"/></svg></span>Learn more</div>
</article>
<article class="card abs" style="left:465px">
  <div class="card-photo" role="img" aria-label="Coal loading port with a ship and conveyor structures under a blue sky" style="background:linear-gradient(#9fb8d0 0%,#c8d4de 45%,#4a5560 70%,#2a3440 100%)"></div>
  <hr><h3>Engineering</h3>
  <p>Lorem ipsum dolor sit amet, consectetur adipiscing elit. Aliquam ultricies odio magna. Mauris a lacus metus, sed ultrices dui. Vivamus at eros non lectus ultrices rutrum. Sed in neque diam. Nulla varius commodo justo, id consequat nisl lacinia vitae. Proin</p>
  <div class="more"><span><svg width="7" height="8" viewBox="0 0 7 8"><path d="M1 1l4 3-4 3" stroke="#fff" stroke-width="1.5" fill="none"/></svg></span>Learn more</div>
</article>
<article class="card abs" style="left:729px">
  <div class="card-photo" role="img" aria-label="Workers in orange high-visibility gear and white helmets at a mine site" style="background:linear-gradient(90deg,#3a3a3a,#d0601c 45%,#e07a2a 60%,#5a5a5a)"></div>
  <hr><h3>Employee Benifits</h3>
  <p>Lorem ipsum dolor sit amet, consectetur adipiscing elit. Aliquam ultricies odio magna. Mauris a lacus metus, sed ultrices dui. Vivamus at eros non lectus ultrices rutrum. Sed in neque diam. Nulla varius commodo justo, id consequat nisl lacinia vitae. Proin</p>
  <div class="more"><span><svg width="7" height="8" viewBox="0 0 7 8"><path d="M1 1l4 3-4 3" stroke="#fff" stroke-width="1.5" fill="none"/></svg></span>Learn more</div>
</article>

<div class="footer-rule abs"></div>
<footer class="footer-ground abs" role="img" aria-label="Dark scattered coal lumps along the bottom edge"></footer>

<div class="footer-col abs" style="left:203px">
  <h4>Menu</h4>
  <ul class="menu-list">
    <li>Home</li><li>SOP / WPI</li>
    <li>About Us</li><li>Contact Us</li>
    <li>Employee Pay</li><li>Mission statement</li>
  </ul>
</div>
<div class="footer-col abs" style="left:467px">
  <h4>News</h4>
  <div class="news-item"><time>03.05.14</time><span>Vivamus at eros non lectus ultrices rutrum. Sed in neque diam. Nulla</span></div>
  <div class="news-item"><time>03.05.14</time><span>Vivamus at eros non lectus ultrices rutrum. Sed in neque diam. Nulla</span></div>
</div>
<div class="footer-col abs" style="left:729px">
  <h4>Contact Us</h4>
  <div class="contact-row">
    <svg width="12" height="15" viewBox="0 0 12 15"><path d="M6 14C2 9 1 7 1 5.5a5 5 0 0 1 10 0C11 7 10 9 6 14z" stroke="#ddd" stroke-width="1.5" fill="none"/><circle cx="6" cy="5.5" r="1.6" fill="#ddd"/></svg>
    <span>1001 Lorem ipdum dolar sit amet<br>Lorem ipsum,GHUA - 1230</span>
  </div>
  <div class="contact-row">
    <svg width="12" height="18" viewBox="0 0 12 18"><rect x="2" y="1" width="8" height="16" rx="1.5" stroke="#ddd" stroke-width="1.5" fill="none"/><circle cx="6" cy="14" r="1" fill="#ddd"/></svg>
    <span>123-456-7890<br>123-456-7890</span>
  </div>
</div>

<p class="copyright abs">© 2014 Ironvale Shift Services</p>

</body>
</html>
```